CD Design Cover - "Beyond the Orchard Gate"

I need a CD cover design. The original Album or CD was recorded in the early eighties. We are re-mastering it. It needs a fresh cover. The genre' is contemporary Christian music and the title of the album is "Beyond the Orchard Gate." This is referring to caring outside of the church walls. A picture of the solo artist could be integrated in the back design. It is not a good picture and does not have to be used. You would have to be creative in using it because of the quality. It does not have to be used at all. I also added some pictures I liked that could be used. I think I like the "Empty church opening" the best. Fits the theme perfectly.

Target Market(s)

30 years old and older.

Requirements
Must have
• Warmth
Nice to have
• I attached two pictures. One of an empty church and one with a reflection of a stain glass window on the wall. It would be nice to see some offerings using these pictures.
Should not have
• Not too churchy

```html
<!DOCTYPE html>
<html lang="en">
<head>
<meta charset="UTF-8">
<title>Beyond the Orchard Gate – Back Cover</title>
<link rel="stylesheet" href="https://fonts.googleapis.com/css2?family=Barlow:wght@300;400&family=Montserrat:wght@800&display=swap">
<style>
  :root {
    --sky-deep: #1d2a3b;
    --sky-mid: #4b586a;
    --sky-haze: #b9b4a4;
    --sunset-gold: #f2a546;
    --sunset-rose: #c77a62;
    --dusk-violet: #5e5d6a;
    --field-dark: #26311d;
    --field-mid: #35422a;
    --accent-yellow: #ffcc0d;
    --text-light: #eef0f2;
    --number-ink: #2b2a25;
  }
  html, body {
    margin: 0;
    padding: 0;
    width: 1200px;
    height: 1200px;
    overflow: hidden;
  }
  .back-cover {
    position: relative;
    width: 1200px;
    height: 1200px;
    overflow: hidden;
    font-family: "Barlow", sans-serif;
  }
  .landscape-photo {
    position: absolute;
    inset: 0;
    background: linear-gradient(
      to bottom,
      var(--sky-deep) 0%,
      var(--sky-mid) 30%,
      var(--sky-haze) 50%,
      var(--sunset-gold) 66%,
      var(--sunset-rose) 72%,
      var(--dusk-violet) 78%,
      var(--dusk-violet) 85%,
      var(--field-mid) 85%,
      var(--field-dark) 100%
    );
  }
  .tracklist-band {
    position: absolute;
    left: 689px;
    top: 0;
    width: 37px;
    height: 468px;
    background: var(--accent-yellow);
  }
  .tracklist {
    position: absolute;
    left: 689px;
    top: 76px;
    margin: 0;
    padding: 0;
    list-style: none;
  }
  .track {
    display: flex;
    align-items: baseline;
    height: 38.3px;
    font-size: 29px;
    font-weight: 400;
    letter-spacing: 0.3px;
  }
  .track-number {
    width: 37px;
    text-align: center;
    color: var(--number-ink);
  }
  .track-title {
    margin-left: 13px;
    color: var(--text-light);
    text-shadow: 0 0 2px rgba(0, 0, 0, 0.55);
    white-space: nowrap;
  }
  .credits {
    position: absolute;
    left: 78px;
    top: 1049px;
    margin: 0;
  }
  .credit {
    display: flex;
    align-items: baseline;
    height: 28px;
    white-space: nowrap;
  }
  .credit-role {
    font-family: "Barlow", sans-serif;
    font-weight: 300;
    font-size: 21px;
    color: var(--text-light);
    letter-spacing: 0.4px;
    margin-right: 14px;
  }
  .credit-role.is-tight {
    margin-right: 8px;
  }
  .credit-name {
    font-family: "Montserrat", sans-serif;
    font-weight: 800;
    font-size: 20px;
    color: var(--accent-yellow);
    margin: 0;
  }
</style>
</head>
<body>
  <main class="back-cover">
    <div class="landscape-photo" role="img" aria-label="Photograph of a small stone chapel with a steeple on a grassy hill under a dramatic cloudy sunset sky"></div>

    <div class="tracklist-band"></div>
    <ol class="tracklist">
      <li class="track"><span class="track-number">1</span><span class="track-title">MORNING LANTERNS</span></li>
      <li class="track"><span class="track-number">2</span><span class="track-title">BEYOND THE ORCHARD GATE</span></li>
      <li class="track"><span class="track-number">3</span><span class="track-title">NEIGHBOR'S TABLE</span></li>
      <li class="track"><span class="track-number">4</span><span class="track-title">WHEN THE RIVER CARRIED ME</span></li>
      <li class="track"><span class="track-number">5</span><span class="track-title">OPEN HANDS</span></li>
      <li class="track"><span class="track-number">6</span><span class="track-title">STILL WALKING WITH YOU</span></li>
      <li class="track"><span class="track-number">7</span><span class="track-title">SEED AND SPARROW</span></li>
      <li class="track"><span class="track-number">8</span><span class="track-title">WIDER THAN THE FIELD</span></li>
      <li class="track"><span class="track-number">9</span><span class="track-title">BREAD FOR THE ROAD</span></li>
      <li class="track"><span class="track-number">10</span><span class="track-title">WALK THE LONG FIELD</span></li>
    </ol>

    <dl class="credits">
      <div class="credit"><dt class="credit-role">PRODUCER</dt><dd class="credit-name">MARLA PENHALLOW</dd></div>
      <div class="credit"><dt class="credit-role">ENGINEERED</dt><dd class="credit-name">PETER KESTRELMAN</dd></div>
      <div class="credit"><dt class="credit-role is-tight">RECORDED AT</dt><dd class="credit-name">LINDEN HOLLOW STUDIO</dd></div>
      <div class="credit"><dt class="credit-role">PROMOTER</dt><dd class="credit-name">NED FARROW</dd></div>
    </dl>
  </main>
</body>
</html>
```